Dune Air & Plus business card

I need an awesome, double-sided business card designed with our new logo. I would like the one side black with the colored logo, and the back side is all yours. I'd like to see horizontal and vertical layouts. Get creative! Thank you.

Target Market(s)

HVAC, Heating and Cooling in Phoenix, AZ

Industry/Entity Type

HVAC

Contact Information for Business Card

We need our new logo on the card. Tom Harker, (623) 555-0142, tom@trydunesair.com, www.trydunesair.com, ROC 514273

```html
<!DOCTYPE html>
<html lang="en">
<head>
<meta charset="UTF-8">
<title>Dune Air &amp; Plus — Business Card</title>
<link rel="stylesheet" href="https://fonts.googleapis.com/css2?family=Krona+One&family=Michroma&family=Montserrat:wght@500;600&display=swap">
<style>
  :root {
    --backdrop: #e4e4e4;
    --card-black: #1e1b1c;
    --blue-deep: #0b5cb0;
    --blue-light: #3f8fd4;
    --white: #ffffff;
    --orange: #f2812a;
    --red-orange: #e4502b;
  }
  * { margin: 0; padding: 0; box-sizing: border-box; }
  html, body {
    width: 1010px;
    height: 1200px;
    overflow: hidden;
    background: var(--backdrop);
  }
  .sheet {
    position: relative;
    width: 1010px;
    height: 1200px;
  }
  .card {
    position: absolute;
    left: 70px;
    width: 870px;
    height: 500px;
  }
  .card-front {
    top: 62px;
    background: var(--card-black);
    display: flex;
    align-items: center;
    justify-content: center;
    gap: 22px;
  }
  .brand-dot {
    width: 26px;
    height: 26px;
    border-radius: 50%;
    background: var(--orange);
  }
  .brand-name {
    font-family: "Krona One", sans-serif;
    font-size: 50px;
    color: var(--white);
    text-transform: uppercase;
    letter-spacing: 1px;
  }
  .card-back {
    top: 630px;
    background: linear-gradient(90deg, var(--blue-deep) 0%, var(--blue-light) 100%);
    color: var(--white);
    text-align: center;
  }
  .licence {
    position: absolute;
    top: 40px;
    width: 100%;
    font-family: "Montserrat", sans-serif;
    font-weight: 600;
    font-size: 24px;
    letter-spacing: 0.5px;
  }
  .person-name {
    position: absolute;
    top: 82px;
    width: 100%;
    font-family: "Krona One", sans-serif;
    font-size: 86px;
    line-height: 96px;
    text-transform: uppercase;
  }
  .phone {
    position: absolute;
    top: 290px;
    width: 100%;
    font-family: "Michroma", sans-serif;
    font-size: 34px;
    letter-spacing: 2px;
  }
  .contact-line {
    position: absolute;
    top: 458px;
    width: 100%;
    display: flex;
    justify-content: center;
    align-items: center;
    gap: 12px;
    font-family: "Montserrat", sans-serif;
    font-weight: 500;
    font-size: 21px;
  }
  .contact-sep {
    width: 13px;
    height: 13px;
    border-radius: 50%;
    background: var(--orange);
  }
</style>
</head>
<body>
  <main class="sheet">
    <section class="card card-front" aria-label="Card front">
      <span class="brand-dot"></span>
      <span class="brand-name">Dune Air &amp; Plus</span>
    </section>

    <section class="card card-back" aria-label="Card back">
      <p class="licence">ROC 514273</p>
      <h1 class="person-name">Tom<br>Harker</h1>
      <p class="phone">(623) 555-0142</p>
      <p class="contact-line">
        <span class="email">tom@trydunesair.com</span>
        <span class="contact-sep"></span>
        <span class="website">www.trydunesair.com</span>
      </p>
    </section>
  </main>
</body>
</html>
```